OAKandRIVER Learning & Development
Business card, Letterhead & Compliment Slip design
Simple
Mara Hollings
Director
41 Fennick Row
Taplow
South Bucks KX4 7RB
mhollings@oakandriverltd-example.co.uk
www.oakandriverltd-example.co.uk
Letterhead needs to be UK standard size A4 and used electronically, therefore, not too heavy on printer toner.
Compliment slip needs to be DL size which is 110mm x 220mm.
We are open to your ideas on this, it could be that the logo is on the front and all other details on reverse side.
We would like to see your ideas please.
Please see attached file for our logo, to be included in this design project. Many thanks.

```html
<!DOCTYPE html>
<html lang="en">
<head>
<meta charset="utf-8">
<title>OAKandRIVER Stationery Set</title>
<link href="https://fonts.googleapis.com/css2?family=Montserrat:wght@400;600&display=swap" rel="stylesheet">
<style>
:root{
  --backdrop:#8d6c24;
  --ink:#0e0e0e;
  --paper:#ffffff;
  --gold:#b8975a;
  --gold-faint:#efe6d6;
  --rule:#c9b48a;
  --text:#5a5a5a;
}
*{margin:0;padding:0;box-sizing:border-box}
html,body{width:1200px;height:607px;overflow:hidden}
body{background:var(--backdrop);font-family:'Montserrat',sans-serif;position:relative;color:var(--text)}
.sheet{position:absolute;background:var(--paper);box-shadow:0 2px 6px rgba(0,0,0,.25);overflow:hidden}
.band{position:absolute;left:0;right:0;top:0;background:var(--ink)}
.wordmark{position:absolute;font-family:'Montserrat',sans-serif;font-weight:600;color:var(--paper);letter-spacing:.5px;white-space:nowrap;display:flex;align-items:center;gap:5px}
.wordmark .dot{display:inline-block;background:var(--gold);border-radius:50%}
.motif{position:absolute;background:radial-gradient(circle at 50% 50%,var(--gold-faint),#f7f2ea 70%,transparent 72%);opacity:.9}
.footer-rule{position:absolute;left:6%;right:6%;height:1px;background:var(--rule)}
.footer-text{position:absolute;left:0;right:0;text-align:center;font-size:5px;color:var(--text);white-space:nowrap}
.fax-title{position:absolute;font-size:9px;font-weight:600;color:var(--ink);letter-spacing:1px}
.form{position:absolute;border-collapse:collapse;font-size:5px;color:var(--text)}
.form td{border:1px solid #bcbcbc;height:13px;padding:0 3px}
.form td.label{width:34px;background:#f4f4f4}
.checks{position:absolute;display:flex;gap:14px;font-size:5px;color:var(--text)}
.checks span::before{content:"";display:inline-block;width:5px;height:5px;border:1px solid #888;margin-right:3px;vertical-align:-1px}
.card{position:absolute;background:var(--ink);box-shadow:0 2px 5px rgba(0,0,0,.3)}
.card-details{position:absolute;font-size:4.5px;color:var(--gold);line-height:1.5;text-align:right}
.slip-greeting{position:absolute;font-size:6px;color:var(--gold);letter-spacing:1px}
.slip-address{position:absolute;font-size:5px;line-height:1.6;color:var(--text)}
</style>
</head>
<body>

<!-- Fax sheet (behind) -->
<div class="sheet fax-sheet" style="left:420px;top:53px;width:312px;height:518px">
  <div class="band" style="height:62px"></div>
  <div class="wordmark" style="left:96px;top:14px;font-size:11px"><span class="dot" style="width:7px;height:7px"></span>OAKandRIVER</div>
  <div class="fax-title" style="left:268px;top:74px">FAX</div>
  <table class="form" style="left:180px;top:90px;width:122px">
    <tr><td class="label">To:</td><td></td></tr>
    <tr><td class="label">Pages:</td><td></td></tr>
    <tr><td class="label">From:</td><td></td></tr>
    <tr><td class="label">CC:</td><td></td></tr>
  </table>
  <div class="checks" style="left:180px;top:228px"><span>Please Reply</span><span>Please Recycle</span></div>
  <div class="footer-rule" style="bottom:22px"></div>
  <div class="footer-text" style="bottom:12px">41 Fennick Row · Taplow · South Bucks KX4 7RB · 01628 555 010</div>
</div>

<!-- Letterhead front -->
<div class="sheet letterhead" style="left:360px;top:125px;width:300px;height:451px">
  <div class="band" style="height:72px"></div>
  <div class="wordmark" style="left:36px;top:30px;font-size:12px"><span class="dot" style="width:8px;height:8px"></span>OAKandRIVER</div>
  <div class="motif" role="img" aria-label="Faint brand motif decoration" style="left:150px;top:165px;width:135px;height:260px;border-radius:40%"></div>
  <div class="footer-rule" style="bottom:18px"></div>
  <div class="footer-text" style="bottom:8px">41 Fennick Row · Taplow · South Bucks KX4 7RB · www.oakandriverltd-example.co.uk</div>
</div>

<!-- Right back sheet -->
<div class="sheet memo-sheet" style="left:749px;top:120px;width:288px;height:456px">
  <div class="band" style="height:72px"></div>
  <div class="wordmark" style="left:10px;top:30px;font-size:11px"><span class="dot" style="width:7px;height:7px"></span>OAKandRIVER</div>
  <table class="form" style="left:10px;top:122px;width:96px">
    <tr><td class="label">To:</td><td></td></tr>
    <tr><td class="label">Fax:</td><td></td></tr>
    <tr><td class="label">Phone:</td><td></td></tr>
    <tr><td class="label">Re:</td><td></td></tr>
  </table>
  <div class="checks" style="left:10px;top:186px"><span>Urgent</span><span>For Review</span></div>
  <div class="footer-rule" style="bottom:20px"></div>
  <div class="footer-text" style="bottom:10px">41 Fennick Row · Taplow · South Bucks KX4 7RB</div>
</div>

<!-- Right front letterhead -->
<div class="sheet letterhead" style="left:859px;top:48px;width:293px;height:528px">
  <div class="band" style="height:84px"></div>
  <div class="wordmark" style="left:40px;top:36px;font-size:12px"><span class="dot" style="width:8px;height:8px"></span>OAKandRIVER</div>
  <div class="motif" role="img" aria-label="Faint brand motif decoration" style="left:112px;top:270px;width:160px;height:220px;border-radius:40%"></div>
  <div class="footer-rule" style="bottom:18px"></div>
  <div class="footer-text" style="bottom:8px">41 Fennick Row · Taplow · South Bucks KX4 7RB · www.oakandriverltd-example.co.uk</div>
</div>

<!-- Business cards -->
<div class="card card-front" style="left:72px;top:240px;width:132px;height:60px">
  <div class="wordmark" style="left:8px;top:22px;font-size:7px"><span class="dot" style="width:5px;height:5px"></span>OAKandRIVER</div>
  <div class="card-details" style="right:7px;top:12px">Mara Hollings<br>Director</div>
</div>
<div class="card card-back" style="left:216px;top:240px;width:132px;height:60px">
  <div class="wordmark" style="left:26px;top:24px;font-size:8px"><span class="dot" style="width:5px;height:5px"></span>OAKandRIVER</div>
</div>

<!-- Compliment slip -->
<div class="sheet compliment-slip" style="left:24px;top:319px;width:317px;height:264px">
  <div class="band" style="height:77px"></div>
  <div class="wordmark" style="left:20px;top:30px;font-size:12px"><span class="dot" style="width:8px;height:8px"></span>OAKandRIVER</div>
  <div class="slip-greeting" style="left:205px;top:36px">With Compliments</div>
  <div class="slip-address" style="left:20px;top:128px">41 Fennick Row, Taplow, South Bucks KX4 7RB<br>Phone: 01628 555 010 · Mobile: 07700 555 010<br>Email: mhollings@oakandriverltd-example.co.uk</div>
  <div class="motif" role="img" aria-label="Faint brand motif decoration" style="left:222px;top:100px;width:88px;height:140px;border-radius:40%"></div>
  <div class="footer-rule" style="bottom:18px"></div>
  <div class="footer-text" style="bottom:8px">www.oakandriverltd-example.co.uk</div>
</div>

</body>
</html>
```